Cover for software box

Hi, we will sell a product about trading software and we need to create a cover for the software's box. We already have the mockup, we just need the cover and all file that compose it.
We'll need the final render and the .psd file to edit later.

It's a trading script based on cryptocurrencies market, we need this kind of idea in the theme.
It need to be serious, professionnal and attractive, like a VIP product (because it is).
The cover need to reasure the futur client of the seriousness of the company behind it.

The dominant colors are :
Texts :
#1b1b1b
#a9a9a9

Logo :
#b56dd6
#f0e0f4

The box size is 1460x1960 px
The name of the company is "Vorendix"
The better idea will be selected for the next part of the project.
If you are good enough to do design also, we could work together for the next things coming.
Thanks.

```html
<!DOCTYPE html>
<html lang="en">
<head>
<meta charset="utf-8">
<title>Vorendix – Software Box Cover</title>
<link rel="stylesheet" href="https://fonts.googleapis.com/css2?family=Merriweather:wght@400&family=Open+Sans:wght@400;600&display=swap">
<style>
  :root {
    --page-bg: #eceef1;
    --cover-dark: #100d12;
    --cover-dark-2: #1d1421;
    --circuit-violet: #6a2a78;
    --circuit-glow: #b340b0;
    --accent-magenta: #8e268c;
    --accent-light: #f0e0f4;
    --band-bg: #f6f5f8;
    --band-tint: #ece4f1;
    --text-dark: #1b1b1b;
    --text-light: #ffffff;
    --text-muted: #a9a9a9;
  }
  * { box-sizing: border-box; margin: 0; padding: 0; }
  html, body {
    width: 1200px; height: 840px; overflow: hidden;
    background: var(--page-bg);
  }
  .canvas { position: relative; width: 1200px; height: 840px; }
  .box-cover {
    position: absolute; left: 315px; top: 40px;
    width: 570px; height: 760px;
    box-shadow: 0 12px 40px rgba(0,0,0,0.18);
    overflow: hidden;
  }
  .cover-hero {
    position: absolute; left: 0; right: 0; top: 0; height: 485px;
    background: var(--cover-dark);
  }
  .circuit-art {
    position: absolute; inset: 0;
    background:
      radial-gradient(ellipse 45% 35% at 62% 30%, rgba(179,64,176,0.55), transparent 70%),
      radial-gradient(ellipse 40% 40% at 78% 62%, rgba(179,64,176,0.45), transparent 70%),
      radial-gradient(ellipse 35% 45% at 30% 55%, rgba(106,42,120,0.55), transparent 70%),
      radial-gradient(ellipse 30% 25% at 50% 80%, rgba(142,38,140,0.35), transparent 70%),
      linear-gradient(160deg, var(--cover-dark-2) 0%, #2a1730 45%, var(--cover-dark) 100%);
  }
  .brand-mark {
    position: absolute; left: 163px; top: 56px;
    width: 22px; height: 22px;
    background: var(--circuit-glow);
  }
  .brand {
    position: absolute; left: 123px; top: 100px;
    font-family: "Merriweather", Georgia, serif;
    font-size: 30px; font-weight: 400; line-height: 1;
    color: var(--text-light);
  }
  .hero-copy {
    position: absolute; left: 155px; top: 410px; width: 345px;
    font-family: "Open Sans", Arial, sans-serif;
    font-size: 9.5px; line-height: 1.75;
    color: var(--text-light);
  }
  .cover-band {
    position: absolute; left: 0; right: 0; bottom: 0; height: 275px;
    background: var(--band-bg);
  }
  .band-pattern {
    position: absolute; inset: 0;
    background: linear-gradient(90deg, var(--band-tint), var(--band-bg) 40%, var(--band-tint));
  }
  .band-marker {
    position: absolute; left: 0; top: 101px;
    width: 105px; height: 139px;
    background: var(--accent-magenta);
  }
  .band-copy {
    position: absolute; left: 120px; top: 150px; width: 270px;
    font-family: "Open Sans", Arial, sans-serif;
    font-size: 12.5px; line-height: 30px;
    color: var(--text-dark);
  }
  .contact-card {
    position: absolute; right: 6px; top: 77px;
    width: 182px; height: 125px;
    background: var(--accent-magenta);
    padding: 18px 10px 0 12px;
    font-family: "Open Sans", Arial, sans-serif;
    color: var(--text-light);
  }
  .contact-row {
    display: flex; justify-content: space-between; align-items: center;
    height: 31px; font-size: 11px; white-space: nowrap;
  }
  .contact-icon {
    width: 16px; height: 16px; border-radius: 50%; flex: none;
    background: var(--text-light);
    display: flex; align-items: center; justify-content: center;
  }
  .contact-icon svg { width: 10px; height: 10px; }
</style>
</head>
<body>
<main class="canvas">
  <section class="box-cover">
    <div class="cover-hero">
      <div class="circuit-art" role="img" aria-label="Violet and magenta circuit-board lines with streams of digits glowing over a black background"></div>
      <div class="brand-mark"></div>
      <div class="brand">Vorendix</div>
      <p class="hero-copy">Lorem Ipsum is simply dummy text of the printing and typesetting industry. Lorem Ipsum has been the industry's standard dummy text ever since the 1500s, when an unknown printer took a galley of type and scrambled it to make a type specimen</p>
    </div>
    <div class="cover-band">
      <div class="band-pattern" role="img" aria-label="Faint lilac market chart motif on a light background"></div>
      <div class="band-marker"></div>
      <p class="band-copy">Lorem Ipsum is simply dummy text of the printing and typesetting industry. Lorem Ipsum has been the industry's standard dummy text ever since the</p>
      <div class="contact-card">
        <div class="contact-row">
          <span>+99-512870-660281</span>
          <span class="contact-icon"><svg viewBox="0 0 10 10"><path d="M2 1l2 2-1 1.2c.6 1.2 1.4 2 2.6 2.6L6.8 6l2 2-1.2 1.2C4.6 9 1 5.4.8 2.2z" fill="#8e268c"/></svg></span>
        </div>
        <div class="contact-row">
          <span>www.vorendix.io</span>
          <span class="contact-icon"><svg viewBox="0 0 10 10"><circle cx="5" cy="5" r="4" fill="none" stroke="#8e268c" stroke-width="1.2"/><path d="M1 5h8M5 1c2 2.5 2 5.5 0 8M5 1c-2 2.5-2 5.5 0 8" fill="none" stroke="#8e268c" stroke-width="0.9"/></svg></span>
        </div>
        <div class="contact-row">
          <span>Adress Kell 0218 street</span>
          <span class="contact-icon"><svg viewBox="0 0 10 10"><path d="M5 .8a3 3 0 013 3C8 6 5 9.4 5 9.4S2 6 2 3.8a3 3 0 013-3z" fill="#8e268c"/><circle cx="5" cy="3.8" r="1" fill="#fff"/></svg></span>
        </div>
      </div>
    </div>
  </section>
</main>
</body>
</html>
```